Need to make a work slip for trucking company.

I need a form to fill out for my truck drivers to get signed on delivery. It is for a trucking company and this form will be for each machine equipment move. I have included my old sheet which I need Updated. Its going on a 9.5 inch by 8.5 inch sheet of paper. It should have room for the day, date, customer name, ordered by, P.O. Number, Project Number, Driver, Truck/Trailer, Tolls (needs more room then my old sheet need a few lines under each other for each toll during the machine move), Permits, some room for other information, Loads, Hours, and 2 lines for a Signature and Print Line.
Updates

Need to also include a Pickup Address and a Deliver Address with lines to write in. Also I need to add a Print Line (and labeled Print) for whoever is signing the ticket.

Requirements
Must have
• My new company name and Logo. I have included my new Logo. It must be easy to ready. Must include my company colors. (Concrete Gray, and Neon Blue)

```html
<!DOCTYPE html>
<html lang="en">
<head>
<meta charset="utf-8">
<title>Ortega Hauling – Work Ticket</title>
<link href="https://fonts.googleapis.com/css2?family=Roboto:wght@400;500&display=swap" rel="stylesheet">
<style>
  :root {
    --brand-blue: #1a6db5;
    --tint-blue: #c6d5ee;
    --concrete-gray: #8a8a8a;
    --ink: #111111;
    --paper: #ffffff;
  }
  * { margin: 0; padding: 0; box-sizing: border-box; }
  html, body { width: 1200px; height: 1200px; overflow: hidden; background: var(--paper); }
  body { font-family: "Roboto", Arial, sans-serif; color: var(--brand-blue); }
  .ticket { position: relative; width: 1200px; height: 1200px; }
  .abs { position: absolute; }

  .company-name {
    left: 0; width: 1200px; top: 62px; text-align: center;
    font-size: 56px; font-weight: 500; letter-spacing: 3px; color: var(--brand-blue);
  }
  .ticket-no { left: 912px; top: 124px; font-size: 21px; color: var(--ink); }

  .contact-band {
    left: 0; top: 160px; width: 1200px; height: 38px; background: var(--brand-blue);
    color: var(--paper); font-size: 19px; display: flex; align-items: center; justify-content: center;
    white-space: pre;
  }

  .label { font-size: 22px; white-space: nowrap; line-height: 1; }
  .label.bold { font-weight: 500; font-size: 20px; }
  .rule { height: 2px; background: var(--ink); }

  .day { width: 28px; height: 28px; border: 1.5px solid var(--brand-blue); border-radius: 50%;
         display: flex; align-items: center; justify-content: center; font-size: 18px; font-weight: 500; }
  .day.weekend { background: var(--tint-blue); }

  .period { left: 974px; top: 335px; width: 114px; height: 28px; border: 1.5px solid var(--brand-blue); display: flex; }
  .period span { flex: 1; display: flex; align-items: center; justify-content: center; font-size: 17px; font-weight: 500; }
  .period span + span { background: var(--tint-blue); border-left: 1.5px solid var(--brand-blue); }

  .check { width: 26px; height: 26px; border: 1.5px solid var(--ink); top: 407px; }
  .divider { left: 551px; top: 472px; width: 1.5px; height: 248px; background: var(--brand-blue); }

  .remarks { left: 552px; top: 748px; width: 591px; height: 291px; border: 1.5px solid var(--brand-blue); }
  .remarks .label { position: absolute; left: 21px; top: 17px; }

  .tally { top: 1060px; width: 170px; height: 98px; border: 1.5px solid var(--brand-blue); }
  .tally-head { height: 35px; background: var(--tint-blue); border-bottom: 1.5px solid var(--brand-blue);
                display: flex; align-items: center; justify-content: center; font-size: 22px; }
</style>
</head>
<body>
<main class="ticket">
  <h1 class="abs company-name">ORTEGA HAULING</h1>
  <div class="abs ticket-no">Ticket No :</div>

  <div class="abs contact-band">Harbor Point, New York 10990.   |   Phone : (555) 014-2290   |   E-mail : dispatch@ortegahauling.example</div>

  <!-- Header fields -->
  <div class="abs label" style="left:100px;top:237px">Customer</div>
  <div class="abs rule" style="left:199px;top:254px;width:680px"></div>
  <div class="abs label" style="left:912px;top:233px">Date :</div>
  <div class="abs rule" style="left:972px;top:250px;width:165px"></div>

  <div class="abs label" style="left:100px;top:293px">Ordered By</div>
  <div class="abs rule" style="left:211px;top:310px;width:673px"></div>

  <div class="abs day" style="left:924px;top:291px">M</div>
  <div class="abs day" style="left:955px;top:291px">T</div>
  <div class="abs day" style="left:986px;top:291px">W</div>
  <div class="abs day" style="left:1017px;top:291px">T</div>
  <div class="abs day" style="left:1048px;top:291px">F</div>
  <div class="abs day weekend" style="left:1079px;top:291px">S</div>
  <div class="abs day weekend" style="left:1110px;top:291px">S</div>

  <div class="abs period"><span>A.M.</span><span>P.M.</span></div>

  <div class="abs label" style="left:100px;top:348px">P.O. No.</div>
  <div class="abs rule" style="left:180px;top:365px;width:314px"></div>
  <div class="abs label" style="left:504px;top:348px">Project No.</div>
  <div class="abs rule" style="left:622px;top:365px;width:264px"></div>

  <!-- Equipment categories -->
  <div class="abs label bold" style="left:100px;top:410px">F/B</div><div class="abs check" style="left:136px"></div>
  <div class="abs label bold" style="left:204px;top:410px">L/B</div><div class="abs check" style="left:240px"></div>
  <div class="abs label bold" style="left:308px;top:410px">LD</div><div class="abs check" style="left:337px"></div>
  <div class="abs label bold" style="left:405px;top:410px">STR/TRL</div><div class="abs check" style="left:489px"></div>
  <div class="abs label bold" style="left:557px;top:410px">BM/TK</div><div class="abs check" style="left:624px"></div>
  <div class="abs label bold" style="left:692px;top:410px">DUMP TK</div><div class="abs check" style="left:781px"></div>
  <div class="abs label bold" style="left:849px;top:410px">ROLL BACK</div><div class="abs check" style="left:957px"></div>
  <div class="abs label bold" style="left:1025px;top:410px">ROLL OFF</div><div class="abs check" style="left:1117px"></div>

  <!-- Left column -->
  <div class="abs label" style="left:100px;top:477px">Driver</div>
  <div class="abs rule" style="left:173px;top:494px;width:346px"></div>
  <div class="abs label" style="left:100px;top:536px">Tr./Eq.</div>
  <div class="abs rule" style="left:173px;top:553px;width:346px"></div>
  <div class="abs label" style="left:100px;top:595px">L/W/H</div>
  <div class="abs rule" style="left:173px;top:612px;width:346px"></div>
  <div class="abs label" style="left:100px;top:654px">Tolls</div>
  <div class="abs rule" style="left:173px;top:671px;width:346px"></div>
  <div class="abs rule" style="left:173px;top:717px;width:346px"></div>
  <div class="abs rule" style="left:173px;top:763px;width:346px"></div>
  <div class="abs rule" style="left:173px;top:808px;width:346px"></div>
  <div class="abs rule" style="left:173px;top:854px;width:346px"></div>

  <div class="abs label" style="left:100px;top:909px">Permit(s)</div>
  <div class="abs rule" style="left:196px;top:926px;width:321px"></div>
  <div class="abs rule" style="left:186px;top:975px;width:333px"></div>

  <div class="abs label" style="left:100px;top:1021px">Other</div>
  <div class="abs rule" style="left:173px;top:1038px;width:346px"></div>

  <div class="abs tally" style="left:173px"><div class="tally-head">Loads</div></div>
  <div class="abs tally" style="left:350px"><div class="tally-head">Hours</div></div>

  <div class="abs divider"></div>

  <!-- Right column -->
  <div class="abs label" style="left:577px;top:477px">Equipment Type</div>
  <div class="abs rule" style="left:740px;top:494px;width:403px"></div>
  <div class="abs label" style="left:577px;top:550px">Pickup Address</div>
  <div class="abs rule" style="left:732px;top:567px;width:408px"></div>
  <div class="abs rule" style="left:582px;top:611px;width:560px"></div>
  <div class="abs label" style="left:574px;top:655px">Delivery Address</div>
  <div class="abs rule" style="left:739px;top:672px;width:403px"></div>
  <div class="abs rule" style="left:579px;top:717px;width:560px"></div>

  <section class="abs remarks"><div class="label">Remarks</div></section>

  <div class="abs label" style="left:574px;top:1078px">Signature</div>
  <div class="abs rule" style="left:671px;top:1095px;width:471px"></div>
  <div class="abs label" style="left:574px;top:1138px">Print</div>
  <div class="abs rule" style="left:624px;top:1154px;width:516px"></div>
</main>
</body>
</html>
```